Website Design for a Chemical Sales Company

We are working with a Chemical Sales Company in California. They sell various chemicals throughout the US.
Types of products they sell: https://www.wardelguard.example/us/products/all
https://www.molvantra.example/products/kelt/kelthaven-glycol-thermal-fluids/kelthaven-propylene-glycol-thermal-fluids
Some sites to use for inspiration:
https://www.molvantra.example
https://www.kelt.example/en-us
Thank you for taking the time to consider designing a website for us. We are web developers based in Stockton, CA, USA. Most of our projects go through the same process. Understanding this process may help you win a project with us. We custom-code all of our websites in-house. We don’t have any requirements as to what tools you use for your design, but we ask that you follow these guidelines.
IMAGES:
If you use any images or icons in the design, we ask that you have a link to the asset so we can purchase the image/icon. Most of the designs we submit do not have the customer’s images on them unless they have some great images. Be creative; show us the feeling you are trying to portray with your image choices. Use any royalty-free site you choose. We subscribe to Brinmoor and mainly use their images, but we can purchase images outside of Brinmoor. PLEASE NOTE: we will not submit designs to clients with watermarks on the images.
FONTS:
We ask that you identify the fonts you’re using in the design. This can be done in a message if you want. We typically use Pallister Fonts and Brinmoor Fonts.
CONTENT:
We're always open to different content and ideas. We often submit designs with stock images so the client can see our vision. We typically take pictures after the website launch to use their images with our vision. Lorem Ipsum is fine for paragraphs, but we ask that you make the Headers with correct English. We want to be able to show the vision and identify the sections of the website.
INSPIRATION:
We typically add a couple of links in the brief of websites we like to help you get started in your design.
REVISIONS:
We do not often ask for revisions of the designs unless we see something in the design that may not appeal to the client. If there are slight changes that we want to make, we do that in the development process.
FEEDBACK:
We rarely give feedback on designs during the design process. We are working on many website projects and do not have the time to provide feedback. We usually respond if your request is well thought out and asks specific questions, but a note asking “feedback, please” usually goes unanswered.

```html
<!DOCTYPE html>
<html lang="en">
<head>
<meta charset="utf-8">
<title>Ostrivane – Chemical Sales</title>
<link rel="stylesheet" href="https://fonts.googleapis.com/css2?family=Open+Sans:wght@400;600;700&family=Lato:wght@400;700&display=swap">
<style>
:root{
  --navy:#0b4a85;
  --blue:#1a8fe3;
  --link:#1a6fc4;
  --ink:#1b1b1b;
  --muted:#555;
  --page:#f4f5f7;
  --footer:#16181c;
  --footer-bottom:#0f1013;
}
*{box-sizing:border-box;margin:0;padding:0}
html,body{width:1200px;height:2369px;overflow:hidden}
body{position:relative;background:#fff;font-family:'Lato',sans-serif;color:var(--ink)}
.abs{position:absolute}
a{color:inherit;text-decoration:none}

.topbar{left:0;top:0;width:1200px;height:24px;background:var(--navy);color:#fff;font-size:10px}
.topbar span{position:absolute;top:6px;white-space:nowrap}
.flag{display:inline-block;width:14px;height:9px;background:linear-gradient(#c33 0 20%,#fff 20% 40%,#c33 40% 60%,#fff 60% 80%,#c33 80%);vertical-align:-1px;margin-right:5px;position:relative}
.flag::before{content:"";position:absolute;left:0;top:0;width:6px;height:5px;background:#234}

.navbar{left:0;top:24px;width:1200px;height:53px;background:#f5f5f5}
.brand{left:178px;top:16px;font-family:'Open Sans',sans-serif;font-size:15px;color:var(--navy);letter-spacing:.5px;display:flex;align-items:center;gap:6px}
.brand i{width:10px;height:10px;border-radius:50%;background:var(--blue);display:inline-block}
.menu{right:188px;top:20px;display:flex;gap:18px;font-family:'Open Sans',sans-serif;font-size:12px;color:var(--navy)}

.hero{left:0;top:77px;width:1200px;height:530px;background:radial-gradient(ellipse at 80% 40%,#6d8aa3 0%,#3e4a58 35%,#2a2f38 65%,#c9c4c0 100%)}
.finder{left:178px;top:403px;width:238px;height:204px;background:var(--navy);color:#fff;padding:18px 20px}
.finder h2{font-family:'Open Sans',sans-serif;font-weight:400;font-size:18px;line-height:22px}
.finder .search{margin-top:10px;height:19px;background:#fff;border:1px solid #9ab;position:relative}
.finder .search svg{position:absolute;right:4px;top:3px}
.finder ul{list-style:none;display:grid;grid-template-columns:103px 1fr;row-gap:6px;margin-top:20px;font-size:9px}
.finder li{text-decoration:underline;white-space:nowrap}
.finder li::before{content:"▸";font-size:6px;margin-right:5px;vertical-align:1px}

.about{left:426px;top:403px;width:595px;height:204px;background:#fff;padding:36px 23px}
.about h2{font-family:'Open Sans',sans-serif;font-weight:600;font-size:19px}
.about p{font-size:9.3px;line-height:15px;color:var(--muted);margin-top:10px}
.btn{display:inline-flex;align-items:center;gap:6px;margin-top:12px;background:var(--blue);color:#fff;font-family:'Open Sans',sans-serif;font-weight:700;font-size:8px;padding:7px 14px;letter-spacing:.3px}

.h-section{width:1200px;left:0;text-align:center;font-family:'Open Sans',sans-serif;font-weight:600;color:var(--ink)}
.tab{top:696px;height:29px;width:124px;text-align:center;line-height:27px;font-family:'Open Sans',sans-serif;font-size:14px;border:1px solid #ddd}
.tab.on{left:467px;color:var(--link);background:#fff}
.tab.off{left:599px;color:#667;background:#d8d9db;border-color:#d8d9db}

.band{left:0;top:725px;width:1200px;height:377px;background:#fff}
.tile{top:750px;width:278px;height:277px}
.caption{top:1041px;width:278px}
.caption small{display:block;font-size:8.5px;color:var(--link)}
.caption b{display:block;font-family:'Open Sans',sans-serif;font-weight:600;font-size:12.5px;margin-top:8px}
.arrow{top:811px;width:37px;height:172px;background:rgba(40,50,60,.45);display:flex;align-items:center;justify-content:center}
.dots{left:579px;top:1133px;display:flex;gap:5px}
.dots i{width:9px;height:9px;border-radius:2px;background:#222;display:block}
.dots i.on{background:var(--blue)}

.tech{left:0;top:1102px;width:1200px;height:499px;background:var(--page)}
.card{width:198px;height:141px;background:#fff;padding:22px 18px;position:absolute}
.card::after{content:"";position:absolute;right:0;top:0;border-top:9px solid var(--blue);border-left:9px solid transparent}
.card.active{background:var(--blue);color:#fff}
.card.active::after{border-top-color:var(--navy)}
.card b{position:absolute;left:18px;bottom:26px;font-family:'Open Sans',sans-serif;font-weight:600;font-size:12.5px;color:var(--navy);white-space:nowrap}
.card.active b{color:#fff}

.mission{left:0;top:1601px;width:1200px;height:264px;background:linear-gradient(100deg,#2d333b,#464c55 45%,#2f353d 70%,#4a4f56)}
.mission h2{position:absolute;left:202px;top:116px;color:#fff;font-family:'Open Sans',sans-serif;font-weight:600;font-size:19px;line-height:25px}
.help{left:675px;top:1664px;width:320px;height:226px;background:#fff;border-top:5px solid var(--navy);padding:22px 20px}
.help h3{font-family:'Open Sans',sans-serif;font-weight:600;font-size:19px;color:var(--blue)}
.help p.sub{font-family:'Open Sans',sans-serif;font-weight:600;font-size:11px;margin-top:4px;padding-bottom:8px;border-bottom:1px solid #ccc}
.help .grid{display:grid;grid-template-columns:157px 1fr;row-gap:20px;margin-top:30px}
.help .item{display:flex;gap:6px}
.help .item b{display:block;font-family:'Open Sans',sans-serif;font-weight:600;font-size:9.5px;white-space:nowrap}
.help .item a{display:block;font-size:8px;color:var(--link);text-decoration:underline;margin-top:3px;white-space:nowrap}

.divider{left:201px;top:1898px;width:730px;height:1px;background:#e6e6e6}
.partners{left:247px;top:1978px;display:flex;gap:48px;align-items:center}
.partners i{display:block;width:110px;height:32px;background:#dcdde0;border-radius:4px}

.footer{left:0;top:2055px;width:1200px;height:262px;background:var(--footer);border-top:4px solid var(--blue);color:#ccc}
.col{top:49px;font-size:10px}
.col h4{font-family:'Lato',sans-serif;font-weight:700;font-size:12.5px;color:#fff;margin-bottom:10px;white-space:nowrap}
.col li{list-style:none;line-height:22.5px;white-space:nowrap}
.social{display:flex;gap:13px;margin-top:16px}
.social i{width:18px;height:18px;border-radius:3px;background:#fff;display:block}
.bottombar{left:0;top:2317px;width:1200px;height:52px;background:var(--footer-bottom);color:#ccc;font-size:9.5px}
.bottombar span{white-space:nowrap}
</style>
</head>
<body>

<div class="abs topbar">
  <span style="left:694px"><i class="flag"></i>English - US</span>
  <span style="left:821px">Log in / Sign Up</span>
  <span style="left:935px">
    <svg width="10" height="10" viewBox="0 0 24 24" style="vertical-align:-1px;margin-right:4px"><path d="M6 2l4 4-2 3c1 3 4 6 7 7l3-2 4 4-3 4C10 22 2 14 2 5z" fill="none" stroke="#fff" stroke-width="2"/></svg>555 014 2290</span>
</div>

<header class="abs navbar">
  <div class="abs brand"><i></i>Ostrivane</div>
  <nav class="abs menu"><a>Home</a><a>Applications</a><a>Products</a><a>Support</a><a>Contact Us</a></nav>
</header>

<div class="abs hero" role="img" aria-label="Photo of a child in a glittering jacket reaching up into large floating soap bubbles"></div>

<section class="abs finder">
  <h2>The key is to find the right product</h2>
  <div class="search"><svg width="11" height="11" viewBox="0 0 12 12"><circle cx="5" cy="5" r="3.3" fill="none" stroke="#333" stroke-width="1.3"/><path d="M7.5 7.5l3 3" stroke="#333" stroke-width="1.5"/></svg></div>
  <ul>
    <li>Product Catalog</li><li>How to guides</li>
    <li>Technical Library</li><li>Support Videos</li>
    <li>Technical Data</li><li>View Support Articles</li>
    <li>Sheets</li><li>Talk to an Expert</li>
  </ul>
</section>

<section class="abs about">
  <h2>We are building the future</h2>
  <p>There are many variations of passages of Lorem Ipsum available, but the majority have suffered alteration in some form, by injected humour, or randomised words which don't look even slightly believable. If you are going to use a passage of Lorem Ipsum.</p>
  <p style="margin-top:9px">You need to be sure there isn't anything embarrassing hidden in the middle of text. All the Lorem Ipsum generators on the Internet tend to repeat predefined chunks as necessary.</p>
  <a class="btn">KNOW MORE <svg width="10" height="9" viewBox="0 0 10 9"><path d="M0 4.5h8M5 1l3.5 3.5L5 8" fill="none" stroke="#fff" stroke-width="1.5"/></svg></a>
</section>

<h2 class="abs h-section" style="top:640px;font-size:23px">Explore The Market</h2>
<div class="abs tab on">Industry</div>
<div class="abs tab off">Manufacturers</div>

<div class="abs band"></div>
<div class="abs tile" style="left:15px;background:linear-gradient(#3f7bc9,#8fb3de 55%,#b9b7ad)" role="img" aria-label="Photo of a tower crane over a building under construction"></div>
<div class="abs tile" style="left:312px;background:linear-gradient(135deg,#eef0f2,#cfd3d7 60%,#4a4d52)" role="img" aria-label="Photo of an electric car being charged"></div>
<div class="abs tile" style="left:609px;background:linear-gradient(120deg,#f2f4f6,#dfe6ea 50%,#c8d4da)" role="img" aria-label="Photo of laboratory glassware with coloured liquids"></div>
<div class="abs tile" style="left:907px;background:linear-gradient(135deg,#6a4a52,#b48a7c 50%,#e3b9a0)" role="img" aria-label="Photo of a makeup brush over a powder compact"></div>
<div class="abs arrow" style="left:6px"><svg width="22" height="42" viewBox="0 0 22 42"><path d="M20 1L2 21l18 20" fill="none" stroke="#fff" stroke-width="1.5"/></svg></div>
<div class="abs arrow" style="left:1155px"><svg width="22" height="42" viewBox="0 0 22 42"><path d="M2 1l18 20L2 41" fill="none" stroke="#fff" stroke-width="1.5"/></svg></div>

<div class="abs caption" style="left:15px"><small>Enhancing performance and durability</small><b>Construction and manufacturing</b></div>
<div class="abs caption" style="left:311px"><small>High-performance</small><b>Automobile assembly</b></div>
<div class="abs caption" style="left:608px"><small>Solutions for constantly evolving</small><b>Industrial chemical equipments</b></div>
<div class="abs caption" style="left:906px"><small>Exceptional performance</small><b>Beauty and personal care</b></div>

<div class="abs tech"></div>
<div class="abs dots"><i></i><i class="on"></i><i></i></div>
<h2 class="abs h-section" style="top:1172px;font-size:21px;font-family:'Lato',sans-serif;font-weight:400">We Provide The Top Product Technologies</h2>

<div class="card active" style="left:178px;top:1236px">
  <svg width="44" height="44" viewBox="0 0 44 44" fill="none" stroke="#fff" stroke-width="1.8"><rect x="6" y="14" width="16" height="24" rx="3" transform="rotate(20 14 26)"/><path d="M16 6l4 6"/><path d="M34 24c-4 6-4 10 0 12 4-2 4-6 0-12z"/></svg>
  <b>Adhesives and Sealants</b>
</div>
<div class="card" style="left:393px;top:1236px">
  <svg width="44" height="36" viewBox="0 0 44 36" fill="none" stroke="#222" stroke-width="1.8"><rect x="3" y="5" width="38" height="26" rx="2"/><path d="M8 11h28M8 16h28M8 21h28M8 26h28"/></svg>
  <b>Conductive Materials</b>
</div>
<div class="card" style="left:607px;top:1236px">
  <svg width="40" height="42" viewBox="0 0 40 42" fill="none" stroke="#222" stroke-width="1.8"><rect x="6" y="4" width="28" height="34" rx="2"/><circle cx="20" cy="21" r="7"/><path d="M20 17c-2 3-2 5 0 6 2-1 2-3 0-6z"/></svg>
  <b>Lubricants and Fluids</b>
</div>
<div class="card" style="left:822px;top:1236px">
  <svg width="30" height="42" viewBox="0 0 30 42" fill="none" stroke="#222" stroke-width="1.8"><path d="M11 12v10L4 38h22l-7-16V12M9 12h12"/><circle cx="15" cy="4" r="2"/></svg>
  <b>Plastic Additives</b>
</div>
<div class="card" style="left:178px;top:1396px">
  <svg width="44" height="44" viewBox="0 0 44 44" fill="none" stroke="#222" stroke-width="1.8"><rect x="8" y="6" width="26" height="10" rx="2" transform="rotate(35 21 11)"/><path d="M20 22l-8 18M22 22l0 18M24 22l8 18"/></svg>
  <b>Optical Materials</b>
</div>
<div class="card" style="left:393px;top:1396px">
  <svg width="34" height="42" viewBox="0 0 34 42" fill="none" stroke="#222" stroke-width="1.8"><path d="M12 4h10M13 4v10A13 13 0 1 0 21 14V4"/><path d="M6 28h22"/></svg>
  <b>Solvents and Glycols</b>
</div>
<div class="card" style="left:607px;top:1396px">
  <svg width="42" height="44" viewBox="0 0 42 44" fill="none" stroke="#222" stroke-width="1.8"><circle cx="8" cy="6" r="4"/><circle cx="8" cy="38" r="4"/><circle cx="34" cy="22" r="4"/><path d="M10 10l6 12-6 12M16 22h14"/></svg>
  <b>Polymers and Compounds</b>
</div>
<div class="card" style="left:822px;top:1396px">
  <svg width="36" height="42" viewBox="0 0 36 42" fill="none" stroke="#222" stroke-width="1.8"><path d="M14 6h8M15 6v8A14 14 0 1 0 21 14V6"/><circle cx="12" cy="28" r="3"/><circle cx="22" cy="26" r="3"/><circle cx="18" cy="34" r="3"/></svg>
  <b>Foam Control Agents</b>
</div>

<section class="abs mission" role="img" aria-label="Photo of engineers working inside a large aerospace assembly facility">
  <h2>Our mission is to develop<br>the strongest partnership with you</h2>
</section>

<aside class="abs help">
  <h3>Can't find the right product?</h3>
  <p class="sub">We are here to help</p>
  <div class="grid">
    <div class="item"><svg width="14" height="14" viewBox="0 0 14 14" fill="none" stroke="#222"><rect x="2" y="1" width="10" height="12"/><path d="M4 4h6M4 7h6M4 10h4"/></svg><div><b>Ask for a quote</b><a>Quotation form</a></div></div>
    <div class="item"><svg width="14" height="14" viewBox="0 0 14 14" fill="none" stroke="#222"><rect x="2" y="1" width="10" height="12"/><path d="M4 4h6M4 7h6M4 10h6"/></svg><div><b>Request a sample</b><a>Sample request form</a></div></div>
    <div class="item"><svg width="14" height="14" viewBox="0 0 24 24"><path d="M6 2l4 4-2 3c1 3 4 6 7 7l3-2 4 4-3 4C10 22 2 14 2 5z" fill="none" stroke="#222" stroke-width="2"/></svg><div><b>Give us a call</b><a style="text-decoration:none">555 014 2290</a></div></div>
    <div class="item"><svg width="15" height="12" viewBox="0 0 15 12" fill="none" stroke="#222"><rect x="1" y="1" width="13" height="10"/><path d="M1 1l6.5 5L14 1"/></svg><div><b>Drop us a mail</b><a>help@ostrivane.example</a></div></div>
  </div>
</aside>

<div class="abs divider"></div>
<h2 class="abs h-section" style="top:1925px;font-size:18px;font-family:'Lato',sans-serif;font-weight:700">Proudly partnered with</h2>
<div class="abs partners" aria-label="Partner badges"><i></i><i></i><i></i><i></i><i></i></div>

<footer class="abs footer">
  <div class="abs col" style="left:181px"><h4>Get to Know Us</h4><ul><li>Home</li><li>Products</li><li>Product Articles</li><li>Why Ostrivane</li><li>About Us</li><li>Careers</li></ul></div>
  <div class="abs col" style="left:408px"><h4>Let Us Help You</h4><ul><li>Contact Us</li><li>Support</li><li>My Account</li><li>Supplier Login</li><li>News</li></ul></div>
  <div class="abs col" style="left:650px"><h4>Our Policies</h4><ul><li>Conditions of Use</li><li>Cookie Policy</li><li>Manage Cookies</li></ul></div>
  <div class="abs col" style="left:842px"><h4>Connect with Ostrivane</h4><div class="social" aria-label="Social media links"><i></i><i></i><i></i><i></i></div></div>
</footer>
<div class="abs bottombar">
  <span class="abs" style="left:180px;top:20px">Copyright © Ostrivane (2023). All Rights Reserved.</span>
  <span class="abs" style="left:848px;top:20px">Privacy Policy</span>
  <span class="abs" style="left:920px;top:20px">Terms and conditions</span>
</div>

</body>
</html>
```